Harbor Decals
Vending Solutions for your Business
Harbor Decals -
Creative Brief
Bright & Fun-filled
Dale Whitcombe
Owner
24870 Pellwood Lane San Jose, CA 95031
harbor.decals@pellmail.net
Use logo on card and stationary

```html
<!DOCTYPE html>
<html lang="en">
<head>
<meta charset="utf-8">
<title>Harbor Decals – Stationery Set</title>
<link href="https://fonts.googleapis.com/css2?family=Open+Sans:wght@400;700&display=swap" rel="stylesheet">
<style>
  :root {
    --backdrop: #3b3b3b;
    --paper: #ffffff;
    --brand-orange: #f6a42c;
    --brand-orange-deep: #ee8a1c;
    --brand-red: #d6402a;
    --ink: #555555;
    --ink-light: #9a9a9a;
    --card-dark: #1d1d1d;
    --flap-grey: #8c8c8c;
    --flap-grey-light: #d4d4d4;
  }
  * { box-sizing: border-box; margin: 0; padding: 0; }
  html, body { width: 1200px; height: 312px; overflow: hidden; }
  body {
    background: var(--backdrop);
    font-family: "Open Sans", Arial, sans-serif;
    position: relative;
  }
  .sheet { position: absolute; background: var(--paper); box-shadow: 0 1px 3px rgba(0,0,0,.5); overflow: hidden; }

  .brand { display: flex; align-items: center; gap: 4px; }
  .brand-dot { border-radius: 50%; background: var(--brand-orange); flex: none; }
  .brand-name { color: var(--brand-red); font-weight: 700; white-space: nowrap; }

  /* business cards */
  .card { width: 72px; height: 43px; }
  .card--front-light { left: 19px; top: 108px; }
  .card--back-dark { left: 96px; top: 108px; background: var(--card-dark); }
  .card--front-small { left: 19px; top: 160px; }
  .card--back-small { left: 96px; top: 160px; background: var(--card-dark); }
  .card .brand { position: absolute; left: 5px; top: 5px; }
  .card .brand-dot { width: 7px; height: 7px; }
  .card .brand-name { font-size: 6px; }
  .card-details { position: absolute; left: 5px; bottom: 4px; font-size: 2.6px; line-height: 1.4; color: var(--ink); }
  .card--back-dark .card-details, .card--back-small .card-details { color: #cfcfcf; }
  .card-band { position: absolute; left: 0; right: 0; bottom: 0; height: 4px; background: var(--brand-orange); }
  .card-center { position: absolute; inset: 0; display: flex; align-items: center; justify-content: center; }
  .card-center .brand-dot { width: 12px; height: 12px; }

  /* letterheads */
  .letterhead { width: 192px; height: 274px; top: 19px; }
  .letterhead--one { left: 228px; }
  .letterhead--two { left: 444px; }
  .top-band { position: absolute; left: 0; right: 0; top: 0; height: 5px; background: var(--brand-orange); }
  .letterhead .brand { position: absolute; left: 34px; top: 14px; }
  .letterhead .brand-dot { width: 10px; height: 10px; }
  .letterhead .brand-name { font-size: 8px; }
  .letterhead .tagline { position: absolute; left: 48px; top: 26px; font-size: 3px; color: var(--ink-light); }
  .watermark { position: absolute; left: 50%; top: 50%; width: 78px; height: 78px; margin: -39px 0 0 -39px;
    border-radius: 50%; background: radial-gradient(circle, rgba(246,164,44,.22), rgba(246,164,44,.08)); }
  .footer-line { position: absolute; left: 0; right: 0; bottom: 10px; text-align: center; font-size: 2.8px; color: var(--ink-light); }

  /* DL envelope fronts */
  .envelope { width: 209px; height: 125px; left: 667px; }
  .envelope--upper { top: 19px; }
  .envelope--lower { top: 158px; height: 125px; }
  .envelope .brand { position: absolute; left: 12px; top: 14px; }
  .envelope .brand-dot { width: 9px; height: 9px; }
  .envelope .brand-name { font-size: 7px; }
  .envelope .return-address { position: absolute; left: 25px; top: 26px; font-size: 2.6px; color: var(--ink-light); }
  .envelope .footer-line { bottom: 8px; }

  /* envelope backs */
  .envelope-back { left: 888px; width: 288px; }
  .envelope-back--orange { top: 19px; height: 72px; background: linear-gradient(180deg, var(--brand-orange), var(--brand-orange-deep)); }
  .envelope-back--inner { top: 72px; height: 72px; background: var(--paper); }
  .envelope-back--white { top: 150px; height: 140px; }
  .envelope-back svg { position: absolute; left: 0; top: 0; }
  .envelope-back .seal { position: absolute; left: 50%; top: 84px; width: 14px; height: 14px; margin-left: -7px; }
</style>
</head>
<body>

  <!-- business cards -->
  <div class="sheet card card--front-light">
    <div class="brand"><span class="brand-dot"></span><span class="brand-name">Harbor Decals</span></div>
    <div class="card-details">Dale Whitcombe · Owner<br>24870 Pellwood Lane San Jose, CA 95031<br>harbor.decals@pellmail.net</div>
    <div class="card-band"></div>
  </div>
  <div class="sheet card card--back-dark">
    <div class="brand"><span class="brand-dot"></span><span class="brand-name">Harbor Decals</span></div>
    <div class="card-details">Dale Whitcombe · Owner<br>harbor.decals@pellmail.net</div>
  </div>
  <div class="sheet card card--front-small">
    <div class="card-center"><span class="brand-dot"></span></div>
    <div class="card-band"></div>
  </div>
  <div class="sheet card card--back-small">
    <div class="card-center"><span class="brand-dot"></span></div>
  </div>

  <!-- letterheads -->
  <div class="sheet letterhead letterhead--one">
    <div class="top-band"></div>
    <div class="brand"><span class="brand-dot"></span><span class="brand-name">Harbor Decals</span></div>
    <div class="tagline">Vending Solutions for your Business</div>
    <div class="watermark" role="img" aria-label="Faint brand circle"></div>
    <div class="footer-line">24870 Pellwood Lane San Jose, CA 95031 · harbor.decals@pellmail.net</div>
  </div>
  <div class="sheet letterhead letterhead--two">
    <div class="top-band"></div>
    <div class="brand"><span class="brand-dot"></span><span class="brand-name">Harbor Decals</span></div>
    <div class="tagline">Vending Solutions for your Business</div>
    <div class="watermark" role="img" aria-label="Faint brand circle"></div>
    <div class="footer-line">24870 Pellwood Lane San Jose, CA 95031 · harbor.decals@pellmail.net</div>
  </div>

  <!-- envelope fronts -->
  <div class="sheet envelope envelope--upper">
    <div class="top-band"></div>
    <div class="brand"><span class="brand-dot"></span><span class="brand-name">Harbor Decals</span></div>
    <div class="return-address">24870 Pellwood Lane San Jose, CA 95031</div>
    <div class="footer-line">harbor.decals@pellmail.net</div>
  </div>
  <div class="sheet envelope envelope--lower">
    <div class="top-band"></div>
    <div class="brand"><span class="brand-dot"></span><span class="brand-name">Harbor Decals</span></div>
    <div class="return-address">24870 Pellwood Lane San Jose, CA 95031</div>
    <div class="footer-line">harbor.decals@pellmail.net</div>
  </div>

  <!-- envelope backs -->
  <div class="sheet envelope-back envelope-back--orange"></div>
  <div class="sheet envelope-back envelope-back--inner">
    <svg width="288" height="72" viewBox="0 0 288 72" aria-hidden="true">
      <polygon points="0,0 288,0 144,48" fill="var(--flap-grey-light)"/>
      <polygon points="0,0 288,0 144,30" fill="var(--flap-grey)"/>
    </svg>
  </div>
  <div class="sheet envelope-back envelope-back--white">
    <svg width="288" height="140" viewBox="0 0 288 140" aria-hidden="true">
      <polyline points="0,140 144,72 288,140" fill="none" stroke="#e4e4e4" stroke-width="1"/>
      <polygon points="0,0 288,0 144,92" fill="var(--flap-grey)"/>
      <polygon points="0,0 288,0 144,80" fill="#a8a8a8"/>
    </svg>
    <span class="brand-dot seal"></span>
  </div>

</body>
</html>
```